National Virtual accounting firm needs website designed

I need a wordpress website design for a national virtual accounting firm. I will upload my business card, logo, and postcards that I have had designed and followed the same style. I want a similar style to be followed so I can keep the running theme similar.

Services include:

Tax Services:
Tax preparation and planning services for Individuals, businesses, estates, and nonprofits
Full Service Payroll for Businesses
QVT Audit Representation

Consulting:
Entity Selection & Restructuring
Financial Projections & Forecasts
Retirement Planning
IPO Readiness

Accounting:
Bookkeeping
Reviews and Compilations
Payroll Services

Other Services:
CFO Services
Compliance Services
Controller Services
Software Implementations for Tenvolk, Brombalt, and Plovena.

Target Market(s)

small to medium size businesses, and individuals

Industry/Entity Type

accounting firms

Font styles to use
Sans Serif

Colors
59FF00
82FF00
B8FF75
E3FFCB
F4FFEA

Requirements
Must have
• Color schematics from the logo and post cards/business cards

```html
<!DOCTYPE html>
<html lang="en">
<head>
<meta charset="utf-8">
<title>Norvanta — Better Solutions For Your Business</title>
<link href="https://fonts.googleapis.com/css2?family=Montserrat:wght@400;500;600;700;800&display=swap" rel="stylesheet">
<style>
:root{
  --green:#5bb843;
  --green-light:#8cc63f;
  --yellow:#ffcc00;
  --black:#050505;
  --ink:#111111;
  --text:#555555;
  --muted:#888888;
  --grey-bg:#efefef;
  --white:#ffffff;
}
*{box-sizing:border-box;margin:0;padding:0}
html,body{width:1200px;height:3419px;overflow:hidden}
body{font-family:'Montserrat',sans-serif;color:var(--ink);background:var(--white);position:relative}
section,header,footer{position:absolute;left:0;width:1200px}
.btn{position:absolute;display:flex;align-items:center;justify-content:center;background:linear-gradient(90deg,var(--green),var(--green-light));color:var(--white);font-weight:700;font-size:13px;border-radius:4px}

/* hero */
.hero{top:0;height:660px;background:linear-gradient(100deg,#15191c 0%,#262c2f 40%,#4a4f51 70%,#2b2f31 100%);overflow:hidden}
.hero-photo{position:absolute;inset:0;background:radial-gradient(ellipse at 75% 45%,rgba(150,150,140,.35),transparent 60%)}
.brand{position:absolute;display:flex;align-items:center;gap:8px;color:var(--white);font-weight:800;font-size:24px;letter-spacing:.5px}
.brand .dot{width:14px;height:14px;border-radius:50%;background:var(--yellow)}
.hero .brand{left:113px;top:22px}
.nav{position:absolute;top:28px;left:0;font-size:13px;font-weight:500;color:var(--white)}
.nav a{position:absolute;white-space:nowrap;color:var(--white);text-decoration:none}
.nav .active{font-weight:700}
.nav .active::after{content:"";position:absolute;left:-13px;top:38px;width:69px;height:3px;background:var(--yellow)}
.search{position:absolute;left:1070px;top:26px}
.hero h1{position:absolute;left:110px;top:200px;font-size:56px;line-height:60px;font-weight:800;color:var(--white)}
.hero h1 span{color:var(--green-light)}
.hero p{position:absolute;left:112px;top:327px;width:480px;font-size:13.5px;line-height:19px;color:#e8e8e8}
.hero .btn{left:113px;top:411px;width:138px;height:42px}
.play{position:absolute;left:268px;top:400px;width:64px;height:64px;border-radius:50%;border:2px solid var(--white);display:flex;align-items:center;justify-content:center}
.play span{width:46px;height:46px;border-radius:50%;background:var(--white);display:flex;align-items:center;justify-content:center}

/* features */
.features{top:660px;height:258px;background:var(--black);color:var(--white);overflow:hidden}
.feature{position:absolute;top:60px;width:300px}
.feature h3{font-size:13px;font-weight:700;margin:8px 0 18px}
.feature p{font-size:11.5px;line-height:16px}
.divider{position:absolute;top:62px;width:1px;height:134px;background:var(--yellow)}
.flare{position:absolute;right:0;bottom:0;width:240px;height:200px;background:radial-gradient(ellipse at 80% 80%,rgba(110,100,20,.35),transparent 65%)}

/* about */
.about{top:918px;height:664px;border-bottom:1px solid var(--yellow)}
.about .band{position:absolute;left:0;top:0;width:230px;height:663px;background:var(--yellow)}
.photo-main{position:absolute;left:196px;top:73px;width:367px;height:494px;border-radius:12px;background:linear-gradient(160deg,#c9ccd0,#7d8288 55%,#3b3e40);box-shadow:-6px -6px 0 var(--ink)}
.photo-small{position:absolute;left:113px;top:425px;width:170px;height:171px;border:4px solid var(--white);background:linear-gradient(150deg,#d9d4c8,#8a8a84 60%,#c9a640)}
.about h2{position:absolute;left:640px;top:120px;font-size:32px;font-weight:700}
.about .copy{position:absolute;left:640px;top:180px;width:450px;font-size:11.5px;line-height:22px;color:var(--text)}
.about .copy p+p{margin-top:22px}
.ticks{position:absolute;left:640px;top:356px;list-style:none;font-size:13px;color:var(--ink)}
.ticks li{position:relative;padding-left:18px;height:31px}
.ticks li::before{content:"";position:absolute;left:0;top:5px;width:8px;height:8px;border-radius:50%;background:var(--yellow)}
.about .btn{left:640px;top:469px;width:152px;height:42px}

/* services */
.services{top:1582px;height:439px}
.section-title{position:absolute;left:0;width:1200px;text-align:center;font-size:32px;font-weight:700}
.services .section-title{top:55px}
.card{position:absolute;top:119px;width:232px;height:256px;background:var(--white);border-radius:8px;box-shadow:0 4px 20px rgba(0,0,0,.08);padding:40px 25px 0}
.card h3{font-size:15.5px;font-weight:700;margin-top:16px;line-height:19px}
.card p{font-size:10.5px;line-height:15.5px;color:var(--text);margin-top:4px}
.card a{display:inline-block;margin-top:12px;font-size:10px;font-weight:700;color:var(--yellow);border-bottom:1px solid var(--yellow)}
.card.featured{background:linear-gradient(135deg,var(--green),var(--green-light));color:var(--white)}
.card.featured p,.card.featured a{color:var(--white);border-color:var(--white)}

/* help */
.help{top:2021px;height:626px;background:linear-gradient(90deg,#1d2022 0%,#3a3e40 45%,#6a6660 70%,#3f3a36 100%)}
.help h2{position:absolute;left:113px;top:60px;font-size:32px;font-weight:800;color:var(--white)}
.help p{position:absolute;left:113px;top:117px;width:460px;font-size:12px;line-height:22px;color:#e8e8e8}
.help .btn{left:113px;top:231px;width:138px;height:41px}
.why{position:absolute;left:0;top:337px;width:862px;height:289px;background:var(--white)}
.why h2{position:absolute;left:113px;top:55px;font-size:32px;font-weight:800}
.reason{position:absolute;top:132px;font-size:13px;font-weight:700;text-align:left}
.reason svg{display:block;margin-bottom:8px}
.why .divider{top:136px;height:84px}

/* testimonials */
.testimonials{top:2647px;height:547px;background:var(--grey-bg);overflow:hidden}
.testimonials .section-title{top:52px}
.quote{position:absolute;top:120px;height:315px;background:var(--white);border-radius:10px;box-shadow:0 4px 20px rgba(0,0,0,.06);padding:52px 45px 0}
.quote.side{opacity:.55}
.avatar{width:66px;height:66px;border-radius:50%;background:linear-gradient(160deg,#c8c2ba,#6e6a66)}
.quote h4{font-size:15px;font-weight:700;margin-top:16px;letter-spacing:.3px}
.quote .role{font-size:12px;color:var(--yellow);margin:8px 0 6px}
.quote p{font-size:11.5px;line-height:16px;color:var(--text)}
.qmark{position:absolute;right:45px;top:60px}
.stars{position:absolute;right:45px;top:140px;color:var(--yellow);font-size:18px;letter-spacing:3px}
.dots{position:absolute;top:484px;left:540px;display:flex;gap:13px}
.dots span{width:20px;height:4px;border-radius:2px;background:#bbbbbb}
.dots .on{background:var(--ink)}

/* footer */
.footer{top:3194px;height:225px;background:var(--black);color:var(--white);overflow:hidden}
.footer .brand{left:0;width:1200px;justify-content:center;top:26px}
.footer .rule{position:absolute;left:0;top:106px;width:1200px;height:1px;background:var(--yellow)}
.socials{position:absolute;left:514px;top:90px;display:flex;gap:14px}
.socials span{width:32px;height:32px;background:var(--green);border-radius:2px;display:flex;align-items:center;justify-content:center}
.socials i{width:10px;height:10px;border:2px solid var(--white);border-radius:50%}
.footer-nav{position:absolute;top:146px;left:0;width:1200px;display:flex;justify-content:center;gap:34px;font-size:12px}
.footer-nav .active{font-weight:700}
.copyright{position:absolute;top:190px;width:1200px;text-align:center;font-size:10.5px}
</style>
</head>
<body>

<header class="hero">
  <div class="hero-photo" role="img" aria-label="Businesswoman with a tablet walking through a dim modern office, colleague seated at a desk"></div>
  <div class="brand"><span class="dot"></span>NORVANTA</div>
  <nav class="nav">
    <a class="active" style="left:657px">HOME</a>
    <a style="left:730px">ABOUT US</a>
    <a style="left:829px">SERVICES</a>
    <a style="left:924px">CONTACT US</a>
  </nav>
  <svg class="search" width="18" height="18" viewBox="0 0 18 18" fill="none" stroke="#ffcc00" stroke-width="1.6"><circle cx="7.5" cy="7.5" r="5.5"/><path d="M11.5 11.5l4.5 4.5"/></svg>
  <h1>Better Solutions<br>For Your <span>Business</span></h1>
  <p>Lorem ipsum dolor sit amet, consectetur adipiscing elit, sed do eiusmod tempor incididunt ut labore et dolore magna aliqua. Quis ipsum suspendisse ultrices gravida.</p>
  <span class="btn">Learn More</span>
  <div class="play"><span><svg width="14" height="16" viewBox="0 0 14 16"><path d="M1 1l12 7-12 7z" fill="#ffcc00"/></svg></span></div>
</header>

<section class="features">
  <div class="flare"></div>
  <div class="feature" style="left:113px">
    <svg width="36" height="38" viewBox="0 0 36 38" fill="none" stroke="#ffcc00" stroke-width="1.6"><rect x="3" y="2" width="22" height="30" rx="1"/><path d="M8 9h12M8 14h12M8 19h8M20 24l4 10 3-4 4 1-5-9"/></svg>
    <h3>Tax Services</h3>
    <p>Tax preparation and planning services for Individuals, businesses, estates, and nonprofits<br>Full Service Payroll for Businesses<br>QVT Audit Representation</p>
  </div>
  <div class="divider" style="left:435px"></div>
  <div class="feature" style="left:484px">
    <svg width="44" height="38" viewBox="0 0 44 38" fill="none" stroke="#ffcc00" stroke-width="1.6"><path d="M2 3h24v16H12l-6 5v-5H2z"/><path d="M30 12h12v16h-4v5l-6-5H18v-5"/><path d="M7 9h14M7 14h10"/></svg>
    <h3>Consulting</h3>
    <p>Entity Selection &amp; Restructuring Financial Projections &amp; Forecasts Retirement Planning<br>IPO Readiness</p>
  </div>
  <div class="divider" style="left:807px"></div>
  <div class="feature" style="left:856px;top:74px">
    <svg width="32" height="36" viewBox="0 0 32 36" fill="none" stroke="#ffcc00" stroke-width="1.8"><circle cx="16" cy="10" r="8"/><path d="M2 34c0-8 6-13 14-13s14 5 14 13z"/></svg>
    <h3>Accounting</h3>
    <p>Bookkeeping Reviews and Compilations<br>Payroll Services</p>
  </div>
</section>

<section class="about">
  <div class="band"></div>
  <div class="photo-main" role="img" aria-label="Team of colleagues gathered around a laptop at an office table"></div>
  <div class="photo-small" role="img" aria-label="Colleagues talking on a yellow sofa in a lounge"></div>
  <h2>Who We Are</h2>
  <div class="copy">
    <p>Meet our team. I'm a Paragraph. Click here to add your own text and edit me. It's easy. Just click "Edit Text" or double click me and you can start adding your own content and make changes to the font. Feel free to drag and drop me anywhere you like on your page.</p>
    <p>I'm a great place for you to write more. Tell a story and let your users get to know you.Click here to add your own text and edit me.</p>
  </div>
  <ul class="ticks">
    <li>Global Communication</li>
    <li>Save Time &amp; Money</li>
    <li>Completely Secure</li>
  </ul>
  <span class="btn">More About Us</span>
</section>

<section class="services">
  <h2 class="section-title">Service We Provide</h2>
  <div class="card" style="left:113px">
    <svg width="50" height="46" viewBox="0 0 50 46" fill="none" stroke="#ffcc00" stroke-width="1.6"><rect x="2" y="8" width="46" height="36" rx="5"/><path d="M18 8V2h14v6"/><circle cx="25" cy="28" r="9"/><path d="M25 22v12M22 25h5a2 2 0 010 4h-3a2 2 0 000 4h5"/></svg>
    <h3>CFO Services</h3>
    <p>Lorem ipsum dolor sit amet, consectetur adipiscing elit, sed do eiusmod tempor incididunt ut labore et dolore magna aliqua.</p>
    <a>Read More</a>
  </div>
  <div class="card featured" style="left:360px">
    <svg width="52" height="52" viewBox="0 0 52 52" fill="none" stroke="#ffffff" stroke-width="1.6"><circle cx="26" cy="26" r="17"/><circle cx="26" cy="26" r="12"/><path d="M26 2v6M26 44v6M2 26h6M44 26h6M9 9l4 4M39 39l4 4M43 9l-4 4M13 39l-4 4"/><path d="M20 26l4 4 8-8"/></svg>
    <h3>Compliance Services</h3>
    <p>Lorem ipsum dolor sit amet, consectetur adipiscing elit, sed do eiusmod tempor incididunt ut labore et dolore magna aliqua.</p>
    <a>Read More</a>
  </div>
  <div class="card" style="left:607px">
    <svg width="54" height="50" viewBox="0 0 54 50" fill="none" stroke="#ffcc00" stroke-width="1.6"><path d="M4 40L36 8l10 10-32 32z"/><circle cx="30" cy="20" r="4"/><path d="M12 38l2 2M18 32l2 2M42 4a8 8 0 018 8M40 1a12 12 0 0113 13"/></svg>
    <h3>Controller Services</h3>
    <p>Lorem ipsum dolor sit amet, consectetur adipiscing elit, sed do eiusmod tempor incididunt ut labore et dolore magna aliqua.</p>
    <a>Read More</a>
  </div>
  <div class="card" style="left:855px">
    <svg width="56" height="46" viewBox="0 0 56 46" fill="none" stroke="#ffcc00" stroke-width="1.6"><rect x="2" y="4" width="40" height="28" rx="2"/><path d="M16 40h12M22 32v8M14 14l-4 4 4 4M28 14l4 4-4 4M23 12l-4 12"/><circle cx="46" cy="32" r="6"/><circle cx="46" cy="32" r="2"/></svg>
    <h3>Software Implementations</h3>
    <p>Integer suscipit sem et metus sagittis maximus. Quisque lobortis porttitor rhoncus. Vestibulum vitae</p>
    <a>Read More</a>
  </div>
</section>

<section class="help" role="img" aria-label="Colleagues laughing together over laptops in a dark office">
  <h2>What We Can Help For You</h2>
  <p>Lorem ipsum dolor sit amet, consectetur adipiscing elit. Curabitur et magna lacinia, imperdiet diam sed, mollis neque. Maecenas imperdiet auctor lacinia. Duis semper nisl ut est rhoncus, sed congue ante sagittis. Orci varius natoque penatibus et magnis dis parturient montes, nascetur ridiculus mus.</p>
  <span class="btn">Join Us</span>
  <div class="why">
    <h2>Why Choose Us ?</h2>
    <div class="reason" style="left:113px">
      <svg width="40" height="44" viewBox="0 0 40 44" fill="none" stroke="#ffcc00" stroke-width="1.6"><path d="M14 30c-5-3-7-7-7-11a13 13 0 0126 0c0 4-2 8-7 11v5H14z"/><path d="M15 39h10M17 43h6M20 1v4M3 8l3 3M37 8l-3 3M0 20h3M37 20h3"/></svg>
      Exprienced
    </div>
    <div class="divider" style="left:283px"></div>
    <div class="reason" style="left:381px;top:134px">
      <svg width="38" height="46" viewBox="0 0 38 46" fill="none" stroke="#ffcc00" stroke-width="1.6"><circle cx="19" cy="17" r="15"/><circle cx="19" cy="17" r="9"/><path d="M19 11l2 4 4 .5-3 3 .8 4-3.8-2-3.8 2 .8-4-3-3 4-.5z"/><path d="M9 29l-4 13 6-3 4 5 3-12M29 29l4 13-6-3-4 5-3-12"/></svg>
      Professional
    </div>
    <div class="divider" style="left:560px"></div>
    <div class="reason" style="left:657px;top:134px">
      <svg width="44" height="46" viewBox="0 0 44 46" fill="none" stroke="#ffcc00" stroke-width="1.6"><circle cx="24" cy="12" r="9"/><path d="M24 7v10M21 10h5a1.5 1.5 0 010 3h-4a1.5 1.5 0 000 3h5"/><path d="M2 30h8l8-4h10a3 3 0 010 6H20M10 40l6-2h14l12-10-4-3-10 6"/></svg>
      Affordable
    </div>
  </div>
</section>

<section class="testimonials">
  <h2 class="section-title">Testimonial From People</h2>
  <div class="quote side" style="left:-391px;width:643px">
    <div class="avatar" role="img" aria-label="Portrait photo of a client"></div>
    <h4>DELIA FORSGREN</h4>
    <div class="role">Company</div>
    <p>Lorem ipsum dolor sit amet, consectetur adipiscing elit. Praesent tempus dapibus est in porta. Ut erat lacus, feugiat eu suscipit ut, viverra quis lorem. Nulla elit ipsum, gravida in posuereeget, pharetra eget ex. Duis vel mi quis enim finibus laoreet. Vivamus pharetra fermentum faucibus. Etiam ac sapien quis magna imperdiet pretium. Vivamus gravida nisi nec dui placerat, eu</p>
    <svg class="qmark" width="64" height="56" viewBox="0 0 64 56"><path d="M0 0h26v28c0 16-10 26-24 28l-2-8c8-2 12-8 12-14H0zM38 0h26v28c0 16-10 26-24 28l-2-8c8-2 12-8 12-14H38z" fill="#8cc63f"/></svg>
    <div class="stars">★★★★★</div>
  </div>
  <div class="quote" style="left:279px;width:643px">
    <div class="avatar" role="img" aria-label="Portrait photo of a client"></div>
    <h4>DELIA FORSGREN</h4>
    <div class="role">Company</div>
    <p>Lorem ipsum dolor sit amet, consectetur adipiscing elit. Praesent tempus dapibus est in porta. Ut erat lacus, feugiat eu suscipit ut, viverra quis lorem. Nulla elit ipsum, gravida in posuereeget, pharetra eget ex. Duis vel mi quis enim finibus laoreet. Vivamus pharetra fermentum faucibus. Etiam ac sapien quis magna imperdiet pretium. Vivamus gravida nisi nec dui placerat, eu tincidunt eros interdum.</p>
    <svg class="qmark" width="64" height="56" viewBox="0 0 64 56"><path d="M0 0h26v28c0 16-10 26-24 28l-2-8c8-2 12-8 12-14H0zM38 0h26v28c0 16-10 26-24 28l-2-8c8-2 12-8 12-14H38z" fill="#5bb843"/></svg>
    <div class="stars">★★★★★</div>
  </div>
  <div class="quote side" style="left:948px;width:643px">
    <div class="avatar" role="img" aria-label="Portrait photo of a client"></div>
    <h4>DELIA FORSGREN</h4>
    <div class="role">Company</div>
    <p>Lorem ipsum dolor sit amet, consectetur adipiscing elit. Praesent tempus dapibus est in porta. Ut erat lacus, feugiat eu suscipit ut, viverra quis lorem. Nulla elit ipsum, gravida in posuereeget, pharetra eget ex. Duis vel mi quis enim finibus laoreet. Vivamus pharetra fermentum faucibus. Etiam ac sapien quis magna imperdiet pretium. Vivamus gravida nisi nec dui placerat, eu tincidunt eros interdum.</p>
  </div>
  <div class="dots"><span></span><span class="on"></span><span></span><span></span></div>
</section>

<footer class="footer">
  <div class="brand"><span class="dot"></span>NORVANTA</div>
  <div class="rule"></div>
  <div class="socials">
    <span aria-label="Social profile 1"><i></i></span>
    <span aria-label="Social profile 2"><i></i></span>
    <span aria-label="Social profile 3"><i></i></span>
    <span aria-label="Social profile 4"><i></i></span>
  </div>
  <nav class="footer-nav"><span class="active">Home</span><span>About</span><span>Service</span><span>Contact</span></nav>
  <div class="copyright">Copyright © 2010-2023 All rights reserved.</div>
</footer>

</body>
</html>
```